Torvane clean Business Cards

I'm looking for someone to design my business card using my company name and logo. I would like it it be clean, fresh and a little out of the box. The colors I would like used are the same two in my logo (gold and the teal blue color) I also want it to screen high end scene the company name is Torvane clean :) I'm a commercial cleaning company based out of Orange and San Diego county. Once I receive your email I will send over the file. Because the file is quote big with several options of logos. Please be an out of the box thinker and take some risk...I'm looking for someone to put themselves out there. Thanks and good luck

```html
<!DOCTYPE html>
<html lang="en">
<head>
<meta charset="UTF-8">
<title>Torvane Clean Business Cards</title>
<link rel="stylesheet" href="https://fonts.googleapis.com/css2?family=Cinzel:wght@400;500&family=Montserrat:wght@600;800&family=Quicksand:wght@500&display=swap">
<style>
  :root {
    --canvas-bg: #e6e4df;
    --card-bg: #333333;
    --gold: #b9a35c;
    --blue: #1f7fc6;
    --white: #ffffff;
    --card-shadow: rgba(0, 0, 0, 0.25);
  }
  * { box-sizing: border-box; margin: 0; padding: 0; }
  html, body {
    width: 1200px; height: 1000px; overflow: hidden;
    background: var(--canvas-bg);
  }
  .canvas {
    width: 1200px; height: 1000px;
    display: flex; flex-direction: column;
    align-items: center; justify-content: center; gap: 60px;
  }
  .card {
    width: 700px; height: 400px;
    background: var(--card-bg);
    box-shadow: 0 10px 30px var(--card-shadow);
    position: relative;
  }

  /* Front */
  .card-front {
    display: flex; flex-direction: column; justify-content: center;
    padding: 0 60px;
  }
  .brand-lockup {
    display: flex; align-items: center; gap: 22px;
  }
  .brand-mark {
    width: 44px; height: 44px; background: var(--gold); flex: none;
  }
  .brand-name {
    font-family: "Montserrat", sans-serif; font-weight: 800;
    font-size: 70px; letter-spacing: 3px; line-height: 1;
    color: var(--white); text-transform: uppercase;
  }
  .service-line {
    margin-top: 22px;
    font-family: "Montserrat", sans-serif; font-weight: 600;
    font-size: 27px; letter-spacing: 1.5px;
    color: var(--white); text-transform: uppercase;
  }
  .sectors {
    margin-top: 20px;
    font-family: "Cinzel", serif; font-size: 19px; letter-spacing: 1.5px;
    line-height: 1.5; color: var(--gold); text-transform: uppercase;
  }

  /* Back */
  .card-back {
    display: flex; padding: 50px 55px; gap: 40px;
  }
  .back-brand {
    width: 290px; display: flex; flex-direction: column; justify-content: center;
  }
  .back-brand-row { display: flex; align-items: center; gap: 14px; }
  .back-brand-mark { width: 22px; height: 22px; background: var(--gold); }
  .back-brand-name {
    font-family: "Cinzel", serif; font-size: 22px; color: var(--gold);
    letter-spacing: 2px; text-transform: uppercase;
  }
  .motto {
    margin-top: 28px;
    font-family: "Cinzel", serif; font-size: 22px; color: var(--gold);
    letter-spacing: 1px;
  }
  .promise {
    margin-top: 10px;
    font-family: "Quicksand", sans-serif; font-size: 15px; color: var(--white);
  }
  .back-contact {
    flex: 1; display: flex; flex-direction: column; justify-content: center;
    font-family: "Quicksand", sans-serif; font-size: 16px; color: var(--white);
    line-height: 1.55;
  }
  .person-name {
    font-family: "Cinzel", serif; font-size: 24px; color: var(--gold);
    letter-spacing: 1px;
  }
  .person-title { color: var(--blue); margin-bottom: 18px; }
  .label { color: var(--blue); }
  .company-name {
    margin-top: 16px;
    font-family: "Cinzel", serif; font-size: 18px; color: var(--gold);
    letter-spacing: 1px;
  }
</style>
</head>
<body>
<main class="canvas">
  <section class="card card-front">
    <div class="brand-lockup">
      <span class="brand-mark"></span>
      <h1 class="brand-name">Torvane Clean</h1>
    </div>
    <p class="service-line">Commercial Cleaning Services</p>
    <p class="sectors">Office Buildings - Medical Facilities -<br>Schools - Restaurants</p>
  </section>

  <section class="card card-back">
    <div class="back-brand">
      <div class="back-brand-row">
        <span class="back-brand-mark"></span>
        <span class="back-brand-name">Torvane Clean</span>
      </div>
      <p class="motto">"The Torvane Way to Clean"</p>
      <p class="promise">Hard work &amp; dedication is our promise to you!</p>
    </div>
    <div class="back-contact">
      <p class="person-name">YOUR NAME</p>
      <p class="person-title">Title</p>
      <p><span class="label">Phone:</span> 1(800)555-0147</p>
      <p><span class="label">Email:</span> contact@torvanecleanco.com</p>
      <p><span class="label">Website:</span> www.torvane-cleanco.com</p>
      <p class="company-name">TORVANE CLEAN</p>
      <p>4180 Marlow Ave. Harbor Point, CA</p>
    </div>
  </section>
</main>
</body>
</html>
```